Professional business cards for real estate development company

I need business cards for my new real estate development company. The company, "KORVA" is a real estate development, investment, and advisory firm with a focus on multifamily, office, and mixed-use projects across primary and secondary markets in the Southeast United States.

Style preference is modern

Industry/Entity Type

Real Estate Development

Contact Information for Business Card

The business cards need to include:
Name
Title
Mailing Address
Phone Number
Web Address

Logo is attached. I would like white to be the primary color with incorporation of the company colors: #232D3A and #B5A451

Font styles to use
Other font styles liked:
• Montserrat, Avenir

Requirements
Must have
• Company Logo. No need to include the company name since the name is in the logo.
Should not have
• No line type designs

```html
<!DOCTYPE html>
<html lang="en">
<head>
<meta charset="utf-8">
<title>KORVA Business Card</title>
<link rel="stylesheet" href="https://fonts.googleapis.com/css2?family=Montserrat:wght@400;600&display=swap">
<style>
  :root {
    --page-bg: #ecedec;
    --navy: #232d3a;
    --white: #ffffff;
    --gold: #b5a451;
    --gold-deep: #9e8e42;
    --ink: #232d3a;
  }
  * { box-sizing: border-box; margin: 0; padding: 0; }
  html, body {
    width: 1200px;
    height: 976px;
    overflow: hidden;
    background: var(--page-bg);
  }
  .canvas {
    position: relative;
    width: 1200px;
    height: 976px;
  }
  .card {
    position: absolute;
    left: 293px;
    width: 614px;
    height: 354px;
    border-radius: 16px;
    overflow: hidden;
  }
  .card--back {
    top: 118px;
    background: var(--navy);
    display: flex;
    align-items: center;
    justify-content: center;
  }
  .card--front {
    top: 502px;
    background: var(--white);
  }
  .brand {
    display: flex;
    align-items: center;
    gap: 14px;
    font-family: "Montserrat", sans-serif;
    font-weight: 600;
    letter-spacing: 3px;
    line-height: 1;
  }
  .brand__mark { background: var(--gold); }
  .brand--back { color: var(--white); font-size: 56px; }
  .brand--back .brand__mark { width: 18px; height: 18px; }
  .brand--front { color: var(--ink); font-size: 38px; }
  .brand--front .brand__mark { width: 13px; height: 13px; }

  .skyline-band {
    position: absolute;
    left: 0; top: 0;
    width: 100%;
    height: 105px;
    background: linear-gradient(180deg, var(--gold) 0%, var(--gold-deep) 60%, var(--gold-deep) 100%);
  }
  .footer-band {
    position: absolute;
    left: 0; bottom: 0;
    width: 100%;
    height: 21px;
    background: var(--gold);
  }
  .divider {
    position: absolute;
    left: 306px;
    top: 119px;
    width: 2px;
    height: 214px;
    background: var(--gold);
  }
  .logo-area {
    position: absolute;
    left: 24px;
    top: 105px;
    width: 282px;
    height: 228px;
    display: flex;
    align-items: center;
    justify-content: center;
  }
  .contact-list {
    position: absolute;
    left: 368px;
    top: 147px;
    list-style: none;
    font-family: "Montserrat", sans-serif;
    font-size: 13px;
    color: var(--ink);
  }
  .contact-list__item {
    display: flex;
    align-items: center;
    gap: 9px;
    height: 22px;
  }
  .contact-list__item--name {
    font-weight: 600;
    font-size: 14px;
    padding-left: 23px;
  }
  .contact-list__item--title {
    color: var(--gold-deep);
    padding-left: 23px;
    margin-bottom: 6px;
  }
  .contact-list__icon {
    width: 14px;
    height: 14px;
    flex: none;
  }
</style>
</head>
<body>
<main class="canvas">
  <section class="card card--back" aria-label="Card back">
    <div class="brand brand--back">
      <span class="brand__mark"></span>
      <span class="brand__name">KORVA</span>
    </div>
  </section>

  <section class="card card--front" aria-label="Card front">
    <div class="skyline-band" role="img" aria-label="Gold city skyline illustration of office towers"></div>

    <div class="logo-area">
      <div class="brand brand--front">
        <span class="brand__mark"></span>
        <span class="brand__name">KORVA</span>
      </div>
    </div>

    <div class="divider"></div>

    <ul class="contact-list">
      <li class="contact-list__item contact-list__item--name"><span>your name here</span></li>
      <li class="contact-list__item contact-list__item--title"><span>your title here</span></li>
      <li class="contact-list__item">
        <svg class="contact-list__icon" viewBox="0 0 14 14" aria-hidden="true">
          <path d="M1 5 Q7 0 13 5 L11 6.5 L9.5 5 L4.5 5 L3 6.5 Z" fill="#232d3a"/>
          <rect x="3" y="7" width="8" height="6" rx="1" fill="#232d3a"/>
        </svg>
        <span>your contact here</span>
      </li>
      <li class="contact-list__item">
        <svg class="contact-list__icon" viewBox="0 0 14 14" aria-hidden="true">
          <rect x="1" y="3" width="12" height="9" rx="1" fill="#232d3a"/>
          <path d="M2.5 4.5 L7 8.5 L11.5 4.5" fill="none" stroke="#fff" stroke-width="1.3"/>
        </svg>
        <span>your email id here</span>
      </li>
      <li class="contact-list__item">
        <svg class="contact-list__icon" viewBox="0 0 14 14" aria-hidden="true">
          <path d="M7 13 C4 9 3 7 3 5 A4 4 0 0 1 11 5 C11 7 10 9 7 13 Z" fill="#232d3a"/>
          <circle cx="7" cy="5" r="1.6" fill="#fff"/>
        </svg>
        <span>your address here</span>
      </li>
      <li class="contact-list__item">
        <svg class="contact-list__icon" viewBox="0 0 14 14" aria-hidden="true">
          <g fill="none" stroke="#232d3a" stroke-width="1">
            <circle cx="7" cy="7" r="6"/>
            <ellipse cx="7" cy="7" rx="2.6" ry="6"/>
            <line x1="1" y1="7" x2="13" y2="7"/>
            <line x1="2" y1="4" x2="12" y2="4"/>
            <line x1="2" y1="10" x2="12" y2="10"/>
          </g>
        </svg>
        <span>your website here</span>
      </li>
    </ul>

    <div class="footer-band"></div>
  </section>
</main>
</body>
</html>
```